Course Graduation Certificate

This project is not for a flyer but instead for the creation of a course graduation certificate. The final certificate needs to include the Marlowe Summit Aviation Academy logo and the text stating as follows:
Certifies that ___________________________ has satisfactorily completed the course of _______________________________ on ________________________________
I would also like to include some type of gold seal of completion as well as a place to sign my name and credentials at the bottom of the certificate
I have included the Marlowe Summit Aviation Academy logo as well as three other certificate examples for you to work from.
Target Market(s)
Students completing a certification course and receiving a certificate
Look and feel

```html
<!DOCTYPE html>
<html lang="en">
<head>
<meta charset="utf-8">
<title>Course Completion Certificate</title>
<link rel="stylesheet" href="https://fonts.googleapis.com/css2?family=UnifrakturMaguntia&family=Ubuntu:ital,wght@0,500;0,700;1,400;1,500&display=swap">
<style>
  :root {
    --paper: #f3f3f3;
    --blue: #0560ae;
    --orange: #eca862;
    --orange-deep: #b97b3b;
    --bronze: #b87631;
    --white: #ffffff;
    --gold-light: #fbe497;
    --gold-mid: #e7b847;
    --gold-dark: #b4772f;
  }
  * { margin: 0; padding: 0; box-sizing: border-box; }
  html, body { width: 1200px; height: 848px; overflow: hidden; background: var(--paper); }
  .certificate {
    position: relative;
    width: 1200px;
    height: 848px;
    background: var(--paper);
    font-family: "Ubuntu", sans-serif;
    overflow: hidden;
  }
  .brand {
    position: absolute;
    left: 38px;
    top: 58px;
    width: 280px;
    color: var(--blue);
    font-family: "Ubuntu", sans-serif;
    font-weight: 700;
    font-size: 26px;
    line-height: 1.1;
  }
  .title {
    position: absolute;
    left: 0;
    right: 0;
    top: 98px;
    padding-left: 4px;
    text-align: center;
    font-family: "UnifrakturMaguntia", serif;
    font-size: 100px;
    letter-spacing: 8px;
    color: var(--bronze);
    line-height: 1;
    transform: translateX(2px);
  }
  .title span { display: inline-block; margin-left: 0; }
  .accent { position: absolute; }
  .accent-top { left: 0; top: 202px; }
  .accent-bottom { right: 0; top: 605px; }
  .band {
    position: absolute;
    left: 0;
    top: 242px;
    width: 1200px;
    height: 363px;
    background: var(--blue);
  }
  .tab {
    position: absolute;
    top: 363px;
    width: 40px;
    height: 121px;
    background: var(--orange);
  }
  .tab-left { left: 0; border-radius: 0 16px 16px 0; }
  .tab-right { right: 0; border-radius: 16px 0 0 16px; }
  .statement {
    position: absolute;
    left: 277px;
    width: 646px;
    text-align: center;
    font-style: italic;
    color: var(--white);
    white-space: nowrap;
  }
  .lead { top: 276px; font-size: 27px; font-weight: 400; }
  .recipient {
    top: 312px;
    font-size: 45px;
    font-weight: 500;
    color: var(--orange);
    letter-spacing: 1px;
  }
  .rule {
    position: absolute;
    left: 277px;
    width: 646px;
    height: 2px;
    background: var(--orange);
  }
  .rule-name { top: 362px; }
  .rule-course { top: 483px; }
  .completed { top: 396px; font-size: 27px; font-weight: 400; }
  .course {
    top: 440px;
    font-size: 36px;
    font-weight: 500;
    color: var(--orange);
    letter-spacing: 1.5px;
  }
  .date-line { top: 516px; font-size: 27px; font-weight: 400; }
  .date-line .date { color: var(--orange); margin-left: 20px; letter-spacing: 0.5px; }
  .seal { position: absolute; left: 82px; top: 518px; }
  .signature-line {
    position: absolute;
    left: 398px;
    top: 766px;
    width: 404px;
    height: 2px;
    background: var(--orange);
  }
  .signature-label {
    position: absolute;
    left: 398px;
    top: 788px;
    width: 404px;
    text-align: center;
    font-style: italic;
    font-size: 17px;
    letter-spacing: 2px;
    color: var(--bronze);
  }
</style>
</head>
<body>
<main class="certificate">
  <div class="brand">Marlowe Summit Aviation Academy</div>

  <h1 class="title">Certificate</h1>

  <svg class="accent accent-top" width="343" height="40" viewBox="0 0 343 40" aria-hidden="true">
    <polygon points="0,0 321,0 343,40 0,40" fill="var(--orange)"/>
    <polygon points="0,40 321,0 343,40" fill="var(--orange-deep)"/>
  </svg>

  <div class="band"></div>
  <div class="tab tab-left"></div>
  <div class="tab tab-right"></div>

  <svg class="accent accent-bottom" width="342" height="41" viewBox="0 0 342 41" aria-hidden="true">
    <polygon points="0,0 342,0 342,41 20,41" fill="var(--orange)"/>
    <polygon points="0,0 342,0 20,41" fill="var(--orange-deep)"/>
  </svg>

  <p class="statement lead">Certifies that</p>
  <p class="statement recipient">John Doe</p>
  <div class="rule rule-name"></div>
  <p class="statement completed">has satisfactorily completed the course of</p>
  <p class="statement course">lorem Ipsum dolor sit</p>
  <div class="rule rule-course"></div>
  <p class="statement date-line">on <span class="date">February 17, 2025</span></p>

  <svg class="seal" width="178" height="178" viewBox="0 0 178 178" role="img" aria-label="Gold seal of completion">
    <defs>
      <linearGradient id="sealGold" x1="0" y1="0" x2="1" y2="1">
        <stop offset="0" stop-color="var(--gold-mid)"/>
        <stop offset="0.45" stop-color="var(--gold-light)"/>
        <stop offset="1" stop-color="var(--gold-dark)"/>
      </linearGradient>
    </defs>
    <circle cx="89" cy="89" r="89" fill="var(--gold-dark)"/>
    <circle cx="89" cy="89" r="80" fill="var(--gold-mid)"/>
    <circle cx="89" cy="89" r="72" fill="url(#sealGold)"/>
  </svg>

  <div class="signature-line"></div>
  <p class="signature-label">Authorized Signatory</p>
</main>
</body>
</html>
```